Layout für Werbefahnen gesucht
Zielgruppe
Unsere Frühstückpension befindet sich in Jois am Neusiedlersee mit direktem Leithabergblick. Wir haben auch ein Weingut was unsere Gäste sehr schätzen.
Unsere Zielgruppe sind Urlaubsgäste mit höheren Ansprüchen sowie Weinbegeistere , Naturliebhaber, Radfahrer und Seeliebhaber (Neusiedlersee) unser Haus wurde mit sehr hochwertigen Materialien ausgestattet.
Aufgabenstellung
3 STK Werbefahnen ( Fahnenmast stehen schon siehe Beilage Bild) Maße: Format 1000x4000 mm
Unser Logo sollte auf den Fahnen vorhanden sein, man soll erkennen - dass man hier Urlaub verbringen kann und Wein verkosten (genießen) oder auch kaufen kann.
Gerne mit netten kurzen Sprüchen oder Wortspielen (Urlaub mit Leithabergblick oder so?.
Naturverbunden mit liebe zum Wein, die Farben sollten unserem Logo angepasst werden eher naturverbunden braun oder grün, 1 Fahne sollte nur für den Wein gestaltet werden und die anderen beiden für unser Gästehaus.

```html
<!DOCTYPE html>
<html lang="de">
<head>
<meta charset="utf-8">
<title>Werbefahnen – Gut Rebenhang</title>
<link href="https://fonts.googleapis.com/css2?family=Patrick+Hand&display=swap" rel="stylesheet">
<style>
  :root {
    --bg: #ffffff;
    --banner-bg: #ffffff;
    --banner-edge: #e4e1dc;
    --brown: #7a5236;
    --brown-light: #9a7457;
  }
  html, body {
    margin: 0;
    padding: 0;
    width: 1200px;
    height: 967px;
    overflow: hidden;
    background: var(--bg);
  }
  .canvas {
    position: relative;
    width: 1200px;
    height: 967px;
  }
  .banner {
    position: absolute;
    top: 43px;
    width: 218px;
    height: 872px;
    background: var(--banner-bg);
    border: 1px solid var(--banner-edge);
    box-sizing: border-box;
    font-family: "Patrick Hand", cursive;
    color: var(--brown);
  }
  .banner--landscape { left: 247px; }
  .banner--wine { left: 497px; }
  .banner--lake { left: 748px; }
  .banner__photo {
    display: block;
    width: 100%;
    height: 592px;
  }
  .banner--landscape .banner__photo {
    background: linear-gradient(180deg, #d9e6f1 0%, #a9c9e3 30%, #c4d8e6 56%, #4f6b3a 62%, #5b7a36 68%, #a9b43a 74%, #c2c644 100%);
  }
  .banner--wine .banner__photo {
    background: linear-gradient(180deg, #9fc4e4 0%, #b8d2e6 45%, #d4dcd8 56%, #a9a58a 60%, #c9d3d6 63%, #3f5a2c 70%, #2f4524 85%, #4f6a3a 100%);
  }
  .banner--lake .banner__photo {
    background: linear-gradient(180deg, #4e92d4 0%, #8fbbe2 48%, #b6cfe3 52%, #51637a 55%, #7da2c6 58%, #2f5f92 75%, #0f2e55 100%);
  }
  .banner__slogan {
    position: absolute;
    top: 658px;
    left: 0;
    right: 0;
    margin: 0;
    text-align: center;
    font-size: 30px;
    font-weight: 400;
    line-height: 31px;
    letter-spacing: 0.5px;
  }
  .brand {
    position: absolute;
    top: 822px;
    left: 0;
    right: 0;
    text-align: center;
  }
  .brand__name {
    display: block;
    font-size: 24px;
    line-height: 24px;
    letter-spacing: 0.5px;
  }
  .brand__tagline {
    display: block;
    font-size: 11px;
    line-height: 13px;
    letter-spacing: 0.6px;
  }
</style>
</head>
<body>
<main class="canvas">
  <section class="banner banner--landscape">
    <div class="banner__photo" role="img" aria-label="Landschaftsfoto: Blick über ein gelbgrünes Feld und Weinberge zum Leithaberg unter blauem Himmel"></div>
    <h2 class="banner__slogan">Urlaub mit<br>Leithabergblick</h2>
    <div class="brand">
      <span class="brand__name">Gut Rebenhang</span>
      <span class="brand__tagline">Schlafen am Neusiedler See</span>
    </div>
  </section>

  <section class="banner banner--wine">
    <div class="banner__photo" role="img" aria-label="Foto: junge Weinreben mit Pfählen, dahinter Nebel über dem Neusiedler See"></div>
    <h2 class="banner__slogan">Purer<br>Weingenuss</h2>
    <div class="brand">
      <span class="brand__name">Gut Rebenhang</span>
      <span class="brand__tagline">Schlafen am Neusiedler See</span>
    </div>
  </section>

  <section class="banner banner--lake">
    <div class="banner__photo" role="img" aria-label="Foto: Segelhafen am Neusiedler See mit Holzpfählen und Schilf im spiegelnden Wasser"></div>
    <h2 class="banner__slogan">Direkt am<br>Neusiedler See</h2>
    <div class="brand">
      <span class="brand__name">Gut Rebenhang</span>
      <span class="brand__tagline">Schlafen am Neusiedler See</span>
    </div>
  </section>
</main>
</body>
</html>
```